Bref créative
Skyward Valuers - Promotional Handouts
Tri-Fold Brochure and Postcard for direct mail
Two items needed:
1. - Tri-fold Brochure (Letter Size) used for distribution face to face.
2. - Postcard (Standard Size) used for direct mail campaigns.
Use the content in the attached files.
Or feel free to add/delete/change any of the copy, or create your own copy (make sure to spell/grammar check). Keep it within the feel of the company.
This company appraises aircraft (Airplanes, Helicopters, Jets, etc;)
My current website is ( www.skywardval-example.com ) this will give you a sense of what kind of business it is. (Still haven't updated the site with the new logo)
Aviation
These will go out to potential customers/clients who would like to have their aircraft appraised. Usually the people who own aircraft or who need an aircraft appraised are corporate professionals.
I deal with a lot of 'Type A' personalities, people who own aircraft tend to be in the higher income bracket and also have high standards. They will use my company to perform research for aircraft sales and acquisition.
They will use my company as a tool to help them buy/sell an aircraft or to have it appraised for insurance purposes.
I need to present a very high class elegant, professional looking design.
Clean, simple, and elegant.
This is the logo to be used.
The look and feel from the stationary pack to give you a sense of the type of designs I'm looking for.
My Mission statement (Copy to be used if desired)
Airports that I will travel to with no extra fee (Copy to be used if desired)
My contact information (Copy to be used if desired)
The steps to the appraisal process (Copy to be used if desired)
Information regarding the logo (colors, fonts, etc..)

```html
<!DOCTYPE html>
<html lang="en">
<head>
<meta charset="utf-8">
<title>Skyward Valuers – Postcard and Tri-Fold Brochure</title>
<link href="https://fonts.googleapis.com/css2?family=Open+Sans:wght@400;600;800&display=swap" rel="stylesheet">
<style>
:root{
  --stage:#2b2d31;
  --navy:#0c2546;
  --blue:#1d4f88;
  --sky:#7fa6cf;
  --red:#c61f2a;
  --paper:#ffffff;
  --ink:#1f2b3a;
  --mist:#e6ecf3;
}
*{box-sizing:border-box;margin:0;padding:0}
html,body{width:1200px;height:802px;overflow:hidden;background:var(--stage);font-family:"Open Sans",Arial,sans-serif}
.piece{position:absolute;background:var(--paper);overflow:hidden;box-shadow:0 6px 18px rgba(0,0,0,.5)}
.photo{position:absolute}
.photo-jet{background:linear-gradient(180deg,#6f8fb4 0%,#c9d5e2 45%,#8f8a7c 75%,#3d3a35 100%)}
.photo-heli{background:linear-gradient(180deg,#8fb0d4 0%,#d9e2ea 50%,#b8362f 62%,#6b6f5e 80%,#4e5244 100%)}
.photo-airport{background:linear-gradient(180deg,#3e6a9c 0%,#9fbad6 50%,#d5dde6 70%,#6d7a88 100%)}
.photo-planes{background:linear-gradient(180deg,#d8e2ec 0%,#eef2f6 50%,#a9b2ba 100%)}
.brand{color:var(--red);font-weight:800;letter-spacing:.08em;text-transform:uppercase;text-align:center;white-space:nowrap}
.brand::before{content:"";display:inline-block;width:.6em;height:.6em;background:var(--red);border-radius:50%;margin-right:.35em;vertical-align:.05em}
.heading{font-weight:600;color:var(--paper)}
.copy{font-size:6.5px;line-height:1.45;color:var(--paper)}
.dark{color:var(--ink)}
.panel-blue{position:absolute;background:linear-gradient(180deg,var(--blue),var(--navy))}
.swoosh{position:absolute;left:0;width:100%}

/* postcard front */
.postcard-front{left:144px;top:53px;width:360px;height:175px}
.postcard-front .panel-blue{left:0;top:0;width:150px;height:112px;padding:8px 12px}
.postcard-front .heading{font-size:7.5px;margin-bottom:2px}
.postcard-front .copy{line-height:1.35}
.postcard-front .heading + .copy{margin-bottom:5px}
.postcard-front .photo-heli{left:0;top:112px;width:150px;height:63px}
.postcard-front .photo-jet{left:150px;top:48px;width:210px;height:127px}
.postcard-front .brand{position:absolute;left:150px;top:18px;width:210px;font-size:12px}

/* postcard back */
.postcard-back{left:631px;top:53px;width:413px;height:175px}
.postcard-back .brand{position:absolute;left:16px;top:12px;width:170px;font-size:11px}
.postcard-back .heading{position:absolute;left:18px;top:34px;font-size:8px;color:var(--blue)}
.postcard-back .steps{position:absolute;left:18px;top:47px;width:200px}
.postcard-back .steps p{font-size:6px;line-height:1.35;margin-bottom:2px;border-bottom:1px solid var(--mist);padding-bottom:1px}
.stamp{position:absolute;right:16px;top:12px;width:38px;height:44px;border:1px solid var(--blue);color:var(--blue);font-size:5px;font-weight:600;display:flex;align-items:center;justify-content:center}
.postcard-back .divider{position:absolute;left:230px;top:20px;width:1px;height:90px;background:var(--mist)}
.postcard-back .photo-planes{left:0;top:130px;width:260px;height:45px}
.postcard-back .photo-heli{left:260px;top:120px;width:153px;height:55px}

/* brochure outside */
.brochure-outside{left:84px;top:312px;width:473px;height:408px}
.brochure-outside .panel-left{position:absolute;left:0;top:0;width:158px;height:408px}
.brochure-outside .panel-left .brand{margin-top:30px;font-size:11px}
.brochure-outside .panel-left .photo-heli{left:0;top:110px;width:158px;height:220px}
.brochure-outside .panel-left .base{position:absolute;left:0;bottom:0;width:158px;height:78px;background:var(--navy)}
.brochure-outside .panel-mid{left:158px;top:0;width:157px;height:408px;padding:150px 10px 0;text-align:center}
.brochure-outside .panel-mid .heading{font-size:8px;margin-bottom:4px}
.brochure-outside .panel-right{position:absolute;left:315px;top:0;width:158px;height:408px}
.brochure-outside .panel-right .brand{margin-top:30px;font-size:11px}
.brochure-outside .panel-right .photo-jet{left:0;top:95px;width:158px;height:255px}
.brochure-outside .panel-right .base{position:absolute;left:0;bottom:0;width:158px;height:58px;background:linear-gradient(180deg,var(--blue),var(--navy))}

/* brochure inside */
.brochure-inside{left:643px;top:312px;width:473px;height:408px}
.brochure-inside .panel-left{position:absolute;left:0;top:0;width:158px;height:408px;padding:26px 12px 0}
.brochure-inside .panel-left .brand{font-size:11px;margin-bottom:18px}
.brochure-inside .panel-left .heading{font-size:8px;color:var(--blue);margin-bottom:4px}
.brochure-inside .panel-left .list p{font-size:6px;line-height:1.6}
.brochure-inside .panel-mid{position:absolute;left:158px;top:0;width:157px;height:408px;background:var(--paper)}
.brochure-inside .panel-mid .intro{background:linear-gradient(180deg,var(--blue),var(--navy));padding:14px 12px;height:88px}
.brochure-inside .panel-mid .heading{font-size:8px;margin-bottom:4px}
.brochure-inside .panel-mid .photo-airport{left:0;top:88px;width:157px;height:150px}
.brochure-inside .photo-planes{left:0;top:300px;width:315px;height:108px}
.brochure-inside .panel-right{left:315px;top:0;width:158px;height:408px;padding:30px 12px 0}
.brochure-inside .panel-right .heading{font-size:9px;margin-bottom:6px}
.brochure-inside .panel-right .steps p{margin-bottom:8px}
</style>
</head>
<body>

<section class="piece postcard-front">
  <div class="panel-blue">
    <h2 class="heading">Mission Statement</h2>
    <p class="copy">Skyward Valuers delivers accurate, independent aircraft appraisals for owners, buyers and lenders.</p>
    <h2 class="heading">Contact Information</h2>
    <p class="copy">Phone: 555-0142<br>Fax: 555-0143<br>info@skywardval-example.com<br>www.skywardval-example.com</p>
  </div>
  <div class="brand">Skyward Valuers</div>
  <div class="photo photo-jet" role="img" aria-label="Photo of a private jet nose on the runway at sunset"></div>
  <div class="photo photo-heli" role="img" aria-label="Photo of a red and white helicopter on a grass field"></div>
</section>

<section class="piece postcard-back">
  <div class="brand">Skyward Valuers</div>
  <h2 class="heading">Appraisal Process</h2>
  <div class="steps copy dark">
    <p>Step 1 – Request a quote online.</p>
    <p>Step 2 – Share aircraft records.</p>
    <p>Step 3 – On-site inspection.</p>
    <p>Step 4 – Market research.</p>
    <p>Step 5 – Receive your report.</p>
  </div>
  <div class="divider"></div>
  <div class="stamp">STAMP</div>
  <div class="photo photo-planes" role="img" aria-label="Photo of light aircraft parked on an apron"></div>
  <div class="photo photo-heli" role="img" aria-label="Photo of a red helicopter on a grass field"></div>
  <svg class="swoosh" style="top:110px;height:40px" viewBox="0 0 413 40" preserveAspectRatio="none" aria-hidden="true">
    <path d="M0 32 Q200 2 413 10 L413 17 Q200 9 0 40 Z" fill="var(--red)"/>
    <path d="M0 25 Q200 -3 413 5" fill="none" stroke="var(--sky)" stroke-width="2"/>
  </svg>
</section>

<section class="piece brochure-outside">
  <div class="panel-left">
    <div class="brand">Skyward Valuers</div>
    <div class="photo photo-heli" role="img" aria-label="Photo of a red and white helicopter on a grass field"></div>
    <div class="base"></div>
  </div>
  <div class="panel-blue panel-mid">
    <h2 class="heading">Contact Information</h2>
    <p class="copy">Phone: 555-0142<br>Fax: 555-0143<br>info@skywardval-example.com<br>www.skywardval-example.com</p>
  </div>
  <div class="panel-right">
    <div class="brand">Skyward Valuers</div>
    <div class="photo photo-jet" role="img" aria-label="Photo of a private jet nose on the runway at sunset"></div>
    <div class="base"></div>
  </div>
</section>

<section class="piece brochure-inside">
  <div class="panel-left">
    <div class="brand">Skyward Valuers</div>
    <h2 class="heading">Home Airports*</h2>
    <div class="list dark">
      <p>KAAA – Northfield Regional</p>
      <p>KBBB – Pine Valley</p>
      <p>KCCC – Lakeside Municipal</p>
      <p>KDDD – Riverbend Field</p>
      <p>KEEE – Summit County</p>
      <p>KFFF – Harbor Point</p>
      <p>KGGG – Cedar Ridge</p>
      <p>KHHH – Westgate Executive</p>
      <p>KJJJ – Meadowbrook Field</p>
      <p>KKKK – Eastport Regional</p>
      <p style="margin-top:6px">*No travel fee to these airports.</p>
    </div>
  </div>
  <div class="panel-mid">
    <div class="intro">
      <h2 class="heading">Mission Statement</h2>
      <p class="copy">We provide objective, certified aircraft valuations so owners, buyers and insurers can make confident decisions with complete market insight.</p>
    </div>
    <div class="photo photo-airport" role="img" aria-label="Photo of a jet parked at an airport terminal under blue sky"></div>
  </div>
  <div class="photo photo-planes" role="img" aria-label="Photo of small propeller planes lined up on the ramp"></div>
  <svg class="swoosh" style="top:268px;height:50px;width:315px" viewBox="0 0 315 50" preserveAspectRatio="none" aria-hidden="true">
    <path d="M0 44 Q150 4 315 14 L315 24 Q150 14 0 50 Z" fill="var(--red)"/>
    <path d="M0 36 Q150 -2 315 8" fill="none" stroke="var(--sky)" stroke-width="2"/>
  </svg>
  <div class="panel-blue panel-right">
    <h2 class="heading">Appraisal Process:</h2>
    <div class="steps copy">
      <p>A clear process from first call to final report.</p>
      <p>Step 1 – Request a quote online.</p>
      <p>Step 2 – Share aircraft records.</p>
      <p>Step 3 – On-site inspection.</p>
      <p>Step 4 – Market research.</p>
      <p>Step 5 – Receive your report.</p>
    </div>
  </div>
</section>

</body>
</html>
```